Flyer Design for Car Audio and Window Tinting Shop

We are looking for a skilled graphic designer to create a 6x11" flyer for our car audio and window tinting shop. The flyer should promote our services, including car audio installations, same day installation service, upgrades for QVT and Tolvex vehicles, and window tinting. We want the flyer to be visually appealing and informative, showcasing our expertise in car audio and window tinting. AI generated graphics are perfect. Must have exotic car and nice AI generated backgrounds.

After, we will need 4 different advertising versions.
One for window tinting
Car audio installing
Car wrapping
Marvend/ Tolvex upgrades.

Then one flyer covering all services. Very nice graphical flyer. No templates.

Dark colors are fine.

Company name: Kestrel Works

Must have address, phone number, instagram and website

Attached are the graphic types we’re looking for.

Skills required:
- Graphic design
- Adobe Photoshop or Illustrator
- Creative thinking
- Attention to detail

Logo file included.

Designs look the same

• AI Generated Backgrounds.

```html
<!DOCTYPE html>
<html lang="en">
<head>
<meta charset="utf-8">
<title>Kestrel Works – Window Tinting Flyer</title>
<link rel="stylesheet" href="https://fonts.googleapis.com/css2?family=Exo+2:ital,wght@0,700;0,800;1,700;1,800;1,900&display=swap">
<style>
  :root{
    --ink:#050607;
    --accent:#2a9fcd;
    --white:#ffffff;
    --photo-dark:#0e1013;
    --photo-mid:#3c4148;
    --photo-light:#c9ccd0;
    --photo-warm:#b07a5c;
  }
  html,body{margin:0;padding:0;width:1200px;height:2200px;overflow:hidden;background:var(--ink);}
  .flyer{position:relative;width:1200px;height:2200px;overflow:hidden;background:var(--ink);font-family:"Exo 2",Arial,sans-serif;color:var(--white);}
  .backdrop{position:absolute;inset:0;width:1200px;height:2200px;}
  .brand{position:absolute;left:560px;top:1172px;width:585px;text-align:right;}
  .brand-name{font-size:62px;font-weight:800;font-style:italic;letter-spacing:0;line-height:1;margin:0;}
  .brand-tagline{display:inline-block;margin-top:8px;padding:3px 14px;border:2px solid var(--white);border-radius:6px;font-size:21px;font-weight:700;font-style:italic;letter-spacing:1px;}
  .dealer{position:absolute;left:30px;top:1360px;width:360px;text-align:center;}
  .dealer-name{font-size:78px;font-weight:900;font-style:italic;line-height:1;}
  .dealer-line{display:block;font-style:italic;font-weight:800;line-height:1.1;}
  .dealer-line.big{font-size:32px;margin-top:12px;}
  .dealer-line.small{font-size:22px;}
  .service{position:absolute;left:550px;top:1350px;margin:0;font-weight:900;font-style:italic;font-size:118px;line-height:1.12;letter-spacing:3px;}
  .service .first{display:block;color:var(--white);}
  .service .second{display:block;color:var(--accent);}
  .contact{position:absolute;left:0;width:1200px;text-align:center;font-style:italic;font-weight:800;margin:0;}
  .phone{top:1765px;font-size:78px;color:var(--accent);}
  .address{top:1890px;font-size:66px;line-height:1.2;color:var(--white);}
  .web-row{position:absolute;left:170px;top:2078px;display:flex;align-items:center;gap:24px;}
  .website{font-size:44px;font-weight:800;font-style:italic;}
  .social{display:flex;gap:14px;}
  .social span{display:block;width:76px;height:76px;border-radius:50%;background:var(--accent);}
</style>
</head>
<body>
<div class="flyer">
  <svg class="backdrop" viewBox="0 0 432 792" preserveAspectRatio="none">
    <defs>
      <linearGradient id="photoBase" x1="0" y1="0" x2="1" y2="1">
        <stop offset="0" stop-color="var(--photo-mid)"/>
        <stop offset="0.5" stop-color="var(--photo-dark)"/>
        <stop offset="1" stop-color="var(--photo-dark)"/>
      </linearGradient>
      <radialGradient id="photoLight" cx="0.85" cy="0.12" r="0.45">
        <stop offset="0" stop-color="var(--photo-light)" stop-opacity="0.9"/>
        <stop offset="1" stop-color="var(--photo-light)" stop-opacity="0"/>
      </radialGradient>
      <radialGradient id="photoWarm" cx="0.45" cy="0.2" r="0.3">
        <stop offset="0" stop-color="var(--photo-warm)" stop-opacity="0.55"/>
        <stop offset="1" stop-color="var(--photo-warm)" stop-opacity="0"/>
      </radialGradient>
      <radialGradient id="photoLamp" cx="0.3" cy="0.62" r="0.35">
        <stop offset="0" stop-color="var(--photo-light)" stop-opacity="0.45"/>
        <stop offset="1" stop-color="var(--photo-light)" stop-opacity="0"/>
      </radialGradient>
    </defs>
    <g role="img" aria-label="Photo: detailer polishing the headlight of a dark luxury car with a rotary buffer">
      <polygon points="0,0 432,0 432,205 0,555" fill="url(#photoBase)"/>
      <polygon points="0,0 432,0 432,205 0,555" fill="url(#photoLight)"/>
      <polygon points="0,0 432,0 432,205 0,555" fill="url(#photoWarm)"/>
      <polygon points="0,0 432,0 432,205 0,555" fill="url(#photoLamp)"/>
    </g>
    <polygon class="band" points="0,555 432,200 432,285 0,615" fill="var(--accent)"/>
    <polygon class="corner" points="432,715 432,792 345,792" fill="var(--accent)"/>
  </svg>

  <div class="brand">
    <p class="brand-name">KESTREL WORKS</p>
    <span class="brand-tagline">CAR AUDIO &amp; WINDOW TINTING</span>
  </div>

  <div class="dealer">
    <div class="dealer-name">NORVANE</div>
    <span class="dealer-line big">AUTHORIZED</span>
    <span class="dealer-line small">WINDOW FILM DEALER</span>
  </div>

  <h1 class="service"><span class="first">WINDOW</span><span class="second">TINTING</span></h1>

  <p class="contact phone">Call us: 555,014,2290</p>
  <p class="contact address">1180 W ALDER ROAD N<br>DUNMORE, NV 89000</p>

  <div class="web-row">
    <span class="website">www.kestrelworks.com</span>
    <div class="social" aria-label="Social media"><span></span><span></span><span></span></div>
  </div>
</div>
</body>
</html>
```